fun theme dental practice website!

This client LOVES their superhero theme! They are an established pediatric dental practice with multiple locations. They have recently expanded to see adults and do orthodontics. They would like to have a new website design for the adult part of their practice. It should be similar in theme (superhero) but more adult (no sugarbugs!) . Navigation: about, meet the team, treatments, orthodontics, contact
add appointment request feature

Target Market(s)

adults

Industry/Entity Type

Dental

Number of Pages Required

2 page

Requirements
Must have
• home page design and interior page design
• fun and in theme but not too babyish (should it still look like a comic book?)
• appointment request feature
• visual pow
• colors consistent with logo (see attached)
• use the tooth social media icons

```html
<!DOCTYPE html>
<html lang="en">
<head>
<meta charset="utf-8">
<title>Valor Dental &amp; Orthodontics</title>
<link rel="stylesheet" href="https://fonts.googleapis.com/css2?family=Lato:ital,wght@0,400;0,700;0,900;1,900&family=Varela+Round&display=swap">
<style>
:root{
  --red:#e31b23;
  --red-dark:#b5121a;
  --green:#8dc63f;
  --yellow:#fff200;
  --ink:#222;
  --outline:#4a4a00;
  --grey-panel:#efefef;
  --grey-band:#f1f1f1;
  --footer:#1f1f1f;
  --footer-bar:#333;
  --white:#fff;
}
*{box-sizing:border-box;margin:0;padding:0}
html,body{width:1200px;height:2597px;overflow:hidden}
body{font-family:"Lato",sans-serif;color:var(--ink);background:var(--white);position:relative}
.abs{position:absolute}

/* header */
.site-header{position:absolute;left:0;top:0;width:1200px;height:149px;background:linear-gradient(#fff,#ececec)}
.brand{position:absolute;left:81px;top:26px;display:flex;align-items:center;gap:10px}
.brand-mark{width:26px;height:26px;background:var(--red);border-radius:50%}
.brand-name{font-weight:900;font-size:30px;color:var(--red);line-height:1}
.brand-sub{font-weight:900;font-size:15px;color:var(--red);display:block;margin-top:3px}
.call{position:absolute;right:81px;top:8px;display:flex;gap:8px;align-items:flex-start}
.call small{display:block;font-size:13px;font-weight:700}
.call strong{display:block;font-size:19px;color:var(--red);font-weight:900}
.search{position:absolute;left:883px;top:61px;width:236px;height:29px;display:flex;border:1px solid #ddd;background:#fff}
.search span{flex:1;font-size:11px;font-style:italic;color:#aaa;padding:7px 8px}
.search i{width:29px;background:#999;display:flex;align-items:center;justify-content:center}
.main-nav{position:absolute;left:81px;top:106px;width:1038px;height:43px;background:var(--red);display:flex;border-radius:3px 3px 0 0}
.main-nav a{display:flex;align-items:center;justify-content:center;color:#fff;font-size:16px;text-decoration:none;border-right:1px solid rgba(0,0,0,.2)}
.main-nav a.active{background:var(--green);color:var(--red-dark)}

/* hero */
.hero{position:absolute;left:0;top:149px;width:1200px;height:471px;background:linear-gradient(90deg,#c9cfd6 0%,#dfe2e6 45%,#e9c9b4 70%,#d9b29a 100%)}
.hero-title{position:absolute;left:81px;top:132px;font-weight:900;font-style:italic;font-size:44px;color:#f26522;text-shadow:1px 1px 0 #8a1a00}
.hero-sub{position:absolute;left:81px;top:200px;font-size:29px;color:#222}
.btn{display:inline-block;background:var(--red);color:#fff;text-decoration:none;border-radius:3px;box-shadow:0 4px 0 var(--red-dark)}
.hero .btn{position:absolute;left:81px;top:260px;width:153px;height:60px;font-size:22px;line-height:60px;text-align:center}

/* services */
.service{position:absolute;top:672px;width:295px;height:371px}
.service-panel{position:absolute;left:0;top:54px;width:100%;height:317px;background:var(--grey-panel);clip-path:polygon(0 6%,100% 0,100% 100%,0 100%);border-radius:6px}
.service-photo{position:absolute;left:59px;top:0;width:173px;height:171px;background:var(--red);clip-path:polygon(0 0,100% 0,100% 82%,14% 100%,0 88%)}
.service-photo div{position:absolute;inset:7px;clip-path:polygon(0 0,100% 0,100% 80%,14% 100%,0 88%)}
.service h3{position:absolute;top:188px;width:100%;text-align:center;color:var(--red);font-size:19px;font-weight:700}
.service p{position:absolute;top:220px;left:20px;right:20px;text-align:center;font-size:13px;line-height:22px;color:#333}
.service .btn{position:absolute;left:205px;top:305px;width:90px;height:36px;line-height:36px;text-align:center;font-size:14px;font-weight:700}

/* about + video */
.section-title{font-family:"Varela Round",sans-serif;font-weight:400;font-size:33px;color:var(--yellow);
  text-shadow:-1px -1px 0 var(--outline),1px -1px 0 var(--outline),-1px 1px 0 var(--outline),1px 1px 0 var(--outline),2px 2px 0 var(--outline)}
.about{position:absolute;left:81px;top:1125px;width:710px}
.about-head{display:flex;align-items:center;gap:14px;border-bottom:1px solid #ddd;padding-bottom:6px}
.about-head .tag{font-weight:900;font-size:22px;color:var(--red)}
.about p{font-size:14px;line-height:24.5px;margin-top:14px;color:#222}
.about .btn{margin-top:22px;width:90px;height:36px;line-height:36px;text-align:center;font-size:14px;font-weight:700}
.divider{position:absolute;left:819px;top:1136px;width:2px;height:210px;background:#e2e2e2}
.video{position:absolute;left:852px;top:1125px;width:267px}
.video .section-title{border-bottom:1px solid #ddd;padding-bottom:6px}
.video-frame{margin-top:14px;height:168px;position:relative;background:linear-gradient(135deg,#9fb6c6,#d8dee3 60%,#c5a48f)}
.video-bar{position:absolute;left:0;right:0;bottom:0;height:22px;background:#111;display:flex;align-items:center;padding:0 8px;gap:8px}
.video-bar .track{flex:1;height:3px;background:#555;position:relative}
.video-bar .track b{position:absolute;left:0;top:0;height:3px;width:76%;background:var(--red)}

/* team */
.team{position:absolute;left:0;top:1408px;width:1200px;height:442px;background:var(--green)}
.team .section-title{position:absolute;top:38px;width:100%;text-align:center}
.member{position:absolute;top:105px;width:235px;height:240px}
.member-photo{width:235px;height:220px;background:#fff;clip-path:polygon(0 0,100% 0,100% 78%,0 100%);border-radius:8px;position:relative}
.member-photo div{position:absolute;inset:4px;clip-path:polygon(0 0,100% 0,100% 78%,0 100%);background:linear-gradient(160deg,#e9eef2,#c9d2da)}
.member h4{position:absolute;right:0;top:202px;font-size:17px;color:#fff;font-weight:700}
.social{position:absolute;right:0;top:238px;display:flex;gap:18px}
.social span{width:12px;height:12px;border-radius:50%;background:var(--red)}

/* insurance */
.insurance{position:absolute;left:0;top:1850px;width:1200px;height:162px;background:var(--grey-band)}
.ribbon{position:absolute;left:410px;top:-9px;width:381px;height:59px;background:var(--red);border-radius:4px;display:flex;align-items:center;justify-content:center;font-family:"Varela Round",sans-serif;font-size:31px;color:var(--yellow);box-shadow:0 4px 0 var(--red-dark)}
.providers{position:absolute;left:81px;right:81px;top:69px;height:70px;display:flex;align-items:center;justify-content:space-between}
.providers .badge{width:70px;height:70px;background:#555}
.providers span{font-weight:900;font-size:34px;color:#333}
.providers span.thin{font-weight:400;font-size:18px;color:#1f4fa0}

/* booking */
.booking{position:absolute;left:0;top:2012px;width:1200px;height:326px;background:var(--red)}
.booking h2{position:absolute;top:42px;width:100%;text-align:center;font-family:"Varela Round",sans-serif;font-weight:400;font-size:33px;color:var(--yellow)}
.field{position:absolute;width:247px;height:39px;border:1px solid var(--yellow);border-radius:2px;color:var(--yellow);font-size:14px;padding:11px 12px;display:flex;justify-content:space-between;align-items:center}
.submit{position:absolute;left:203px;top:238px;width:794px;height:38px;background:var(--yellow);color:var(--red);font-size:21px;text-align:center;line-height:38px;border-radius:2px}

/* footer */
.site-footer{position:absolute;left:0;top:2338px;width:1200px;height:222px;background:var(--footer);color:#fff}
.site-footer h5{font-size:16px;font-weight:700;padding-bottom:10px;border-bottom:1px solid #3c3c3c;margin-bottom:14px}
.quick{position:absolute;left:81px;top:14px;width:290px}
.quick ul{list-style:none;display:grid;grid-template-columns:144px 144px;grid-template-rows:repeat(4,34px);grid-auto-flow:column;font-size:13px;line-height:34px}
.quick li::before{content:"\25B8";margin-right:8px;font-size:10px}
.contact{position:absolute;left:455px;top:14px;width:270px}
.contact h5{width:230px}
.contact p{font-size:13px;line-height:20px;display:flex;gap:12px;margin-bottom:18px;white-space:nowrap}
.contact svg{flex:none;margin-top:3px}
.map-col{position:absolute;left:836px;top:14px}
.map-col h5{font-weight:400;border:none;margin-bottom:6px}
.map{width:204px;height:105px;background:linear-gradient(135deg,#efe6c8,#dcd7c9 50%,#e9e2cf)}
.footer-col-line{position:absolute;top:30px;width:1px;height:160px;background:#333}
.copyright{position:absolute;left:0;top:2560px;width:1200px;height:37px;background:var(--footer-bar);color:#ccc;font-size:13px;text-align:center;line-height:37px}
</style>
</head>
<body>

<header class="site-header">
  <div class="brand">
    <span class="brand-mark"></span>
    <div><span class="brand-name">VALOR</span><span class="brand-sub">Dental &amp; Orthodontics</span></div>
  </div>
  <div class="call">
    <svg width="22" height="22" viewBox="0 0 24 24"><circle cx="12" cy="12" r="11" fill="none" stroke="#222" stroke-width="1.5"/><path d="M8 6c-1 1-1 3 1 6s4 5 6 5l1-2-2-2-1 1c-1-.5-2.5-2-3-3l1-1-2-2z" fill="#222"/></svg>
    <div><small>Call Us Today</small><strong>555-014-2368</strong></div>
  </div>
  <div class="search"><span>Search here..</span><i><svg width="13" height="13" viewBox="0 0 14 14"><circle cx="6" cy="6" r="4.5" fill="none" stroke="#fff" stroke-width="2"/><path d="M9.5 9.5l3.5 3.5" stroke="#fff" stroke-width="2"/></svg></i></div>
  <nav class="main-nav">
    <a href="#" style="width:83px"></a>
    <a href="#" class="active" style="width:110px">Home</a>
    <a href="#" style="width:133px">About Us</a>
    <a href="#" style="width:175px">Meet the team</a>
    <a href="#" style="width:142px">Treatments</a>
    <a href="#" style="width:164px">Orthodontics</a>
    <a href="#" style="width:148px">Contact Us</a>
  </nav>
</header>

<section class="hero" role="img" aria-label="Smiling young woman with braces resting her chin on her hands">
  <h1 class="hero-title">Creating Smiles Everyday</h1>
  <p class="hero-sub">A Smile Changes Everything</p>
  <a href="#" class="btn">Get To Know</a>
</section>

<section>
  <article class="service" style="left:81px">
    <div class="service-panel"></div>
    <div class="service-photo"><div role="img" aria-label="Laughing child" style="background:linear-gradient(135deg,#f3d9c4,#d9a985)"></div></div>
    <h3>Kids Dental</h3>
    <p>Lorem ipsum dolor sit amet, consectetuer adipiscing elit, sed diam nonummy nibh euismod tincidunt ut laor</p>
    <a href="#" class="btn">Read More</a>
  </article>
  <article class="service" style="left:452px">
    <div class="service-panel"></div>
    <div class="service-photo"><div role="img" aria-label="Adult patient having a dental check-up" style="background:linear-gradient(135deg,#e9d0c0,#bf8f78)"></div></div>
    <h3>Adults Dental</h3>
    <p>Lorem ipsum dolor sit amet, consectetuer adipiscing elit, sed diam nonummy nibh euismod tincidunt ut laor</p>
    <a href="#" class="btn">Read More</a>
  </article>
  <article class="service" style="left:824px">
    <div class="service-panel"></div>
    <div class="service-photo"><div role="img" aria-label="Close-up of teeth with braces" style="background:linear-gradient(135deg,#f1d7d2,#c9a8a4)"></div></div>
    <h3>Orthodontics</h3>
    <p>Lorem ipsum dolor sit amet, consectetuer adipiscing elit, sed diam nonummy nibh euismod tincidunt ut laor</p>
    <a href="#" class="btn">Read More</a>
  </article>
</section>

<section class="about">
  <div class="about-head"><h2 class="section-title">About</h2><span class="tag">VALOR</span></div>
  <p>Lorem ipsum dolor sit amet, consectetuer adipiscing elit, sed diam nonummy nibh euismod tincidunt ut laoreet dolore magna aliquam erat volutpat. Ut wisi enim Lorem ipsum dolor sit amet, consectetuer adipiscing elit, sed diam nonummy nibh euismod tincidunt ut laoreet dolore magna aliquam erat volutpat. Lorem ipsum dolor sit amet, consectetuer adipiscing elit, sed diam nonummy nibh euismod tincidunt ut laoreet dolore magna aliquam erat volutpat. Lorem ipsum dolor sit amet, consectetuer adipiscing elit.</p>
  <a href="#" class="btn">Read More</a>
</section>
<div class="divider"></div>
<section class="video">
  <h2 class="section-title">Watch Video</h2>
  <div class="video-frame" role="img" aria-label="Dentist examining a young patient">
    <svg class="abs" style="left:120px;top:62px" width="26" height="26" viewBox="0 0 26 26"><circle cx="13" cy="13" r="13" fill="#e31b23"/><path d="M10 8l8 5-8 5z" fill="#fff"/></svg>
    <div class="video-bar">
      <svg width="8" height="10"><rect width="3" height="10" fill="#fff"/><rect x="5" width="3" height="10" fill="#fff"/></svg>
      <div class="track"><b></b></div>
      <svg width="40" height="8"><rect width="30" height="3" y="2" fill="#555"/><circle cx="34" cy="4" r="4" fill="#fff"/></svg>
    </div>
  </div>
</section>

<section class="team">
  <h2 class="section-title">Meet Our Team</h2>
  <article class="member" style="left:81px"><div class="member-photo"><div role="img" aria-label="Portrait of smiling male dentist"></div></div><h4>Dr. Owen Hale</h4><div class="social"><span></span><span></span><span></span></div></article>
  <article class="member" style="left:348px"><div class="member-photo"><div role="img" aria-label="Portrait of smiling female dentist"></div></div><h4>Dr. Clara Fenn</h4><div class="social"><span></span><span></span><span></span></div></article>
  <article class="member" style="left:617px"><div class="member-photo"><div role="img" aria-label="Portrait of male dentist in white coat"></div></div><h4>Dr. Owen Hale</h4><div class="social"><span></span><span></span><span></span></div></article>
  <article class="member" style="left:885px"><div class="member-photo"><div role="img" aria-label="Portrait of female dentist in the clinic"></div></div><h4>Dr. Clara Fenn</h4><div class="social"><span></span><span></span><span></span></div></article>
</section>

<section class="insurance">
  <div class="ribbon">Insurance Providers</div>
  <div class="providers">
    <div class="badge" role="img" aria-label="Provider badge"></div>
    <span>SmileCredit</span>
    <span class="thin">HealthBridge Advance</span>
    <span>KIDPLAN</span>
    <span>CORVEX</span>
  </div>
</section>

<section class="booking">
  <h2>Book An Appointment</h2>
  <div class="field" style="left:203px;top:127px">First Name</div>
  <div class="field" style="left:475px;top:127px">Last Name</div>
  <div class="field" style="left:750px;top:127px">Phone</div>
  <div class="field" style="left:203px;top:182px">Email</div>
  <div class="field" style="left:475px;top:182px">Date<svg width="16" height="16" viewBox="0 0 16 16"><rect x="1" y="2" width="14" height="13" fill="none" stroke="#fff200" stroke-width="1.3"/><path d="M1 6h14M5 9h2M9 9h2M5 12h2M9 12h2" stroke="#fff200" stroke-width="1.3"/></svg></div>
  <div class="field" style="left:750px;top:182px">Time<svg width="17" height="17" viewBox="0 0 18 18"><circle cx="9" cy="9" r="7.5" fill="none" stroke="#fff200" stroke-width="1.5"/><path d="M9 4v5h4" fill="none" stroke="#fff200" stroke-width="1.5"/></svg></div>
  <div class="submit">Book An Appointment</div>
</section>

<footer class="site-footer">
  <div class="quick">
    <h5>Quick Links</h5>
    <ul><li>Home</li><li>About Us</li><li>Meet the team</li><li>Treatment</li><li>Orthodontics</li><li>Contact Us</li></ul>
  </div>
  <div class="footer-col-line" style="left:380px"></div>
  <div class="contact">
    <h5>Contact Details</h5>
    <p><svg width="10" height="14" viewBox="0 0 10 14"><path d="M5 0a5 5 0 0 1 5 5c0 4-5 9-5 9S0 9 0 5a5 5 0 0 1 5-5z" fill="#fff"/><circle cx="5" cy="5" r="2" fill="#1f1f1f"/></svg><span>Valor Dental<br>Lorem Ipsum,dolor, City -Code- 1234</span></p>
    <p><svg width="10" height="14" viewBox="0 0 10 14"><rect x="1" y="0" width="8" height="14" rx="1.5" fill="#fff"/><rect x="2.5" y="2" width="5" height="8" fill="#1f1f1f"/></svg><span>555-014-2368</span></p>
    <p><svg width="13" height="10" viewBox="0 0 13 10"><rect width="13" height="10" fill="#fff"/><path d="M0 0l6.5 5L13 0" fill="none" stroke="#1f1f1f"/></svg><span>info@valordental.com</span></p>
  </div>
  <div class="footer-col-line" style="left:760px"></div>
  <div class="map-col">
    <h5>Location Map</h5>
    <div class="map" role="img" aria-label="Street map showing the practice location"></div>
  </div>
</footer>
<div class="copyright">Copyright © 2016 Valor Dental &amp; Orthodontics.  All Rights Reserved.</div>

</body>
</html>
```